Irrigation Business needs their business cards modernised and revamped

I would like to keep my current logo, colours and revamp the format of the card.

I would like the card to be clean yet important.

Im not sure if you include texture but i would like the named logo to be indented into the card etc.

show me something alive and free something thats clinical to the point yet has a feel of achievement. i would like people to go nice card.

Target Market(s)

high end clients, corporate, sports field manger, the guys that make the decisions

Industry/Entity Type

Business

Contact Information for Business Card

nformation to be included

Dorian Hesk (Director)
0487253916
dorian@tfcraft.biz
www.taddsfieldcrafts.com

instagram logo
google logo
facebook logo

Colors

Designer to choose colors to be used in the design.

Requirements
Nice to have
• indentations a really nice feel to the card good texture

```html
<!DOCTYPE html>
<html lang="en">
<head>
<meta charset="utf-8">
<title>Tadd's Field Crafts — Business Card</title>
<link rel="stylesheet" href="https://fonts.googleapis.com/css2?family=Open+Sans:wght@400;600;700&display=swap">
<style>
  :root {
    --stage: #3a3b3d;
    --card-dark: #17181a;
    --card-light: #f7f7f5;
    --brand-blue: #2f7fc4;
    --brand-sky: #3aa6dc;
    --brand-green: #2fae5a;
    --ink-grey: #5b5d60;
    --rule-blue: #6d9fd0;
  }
  * { box-sizing: border-box; margin: 0; padding: 0; }
  html, body { width: 1200px; height: 840px; overflow: hidden; }
  body {
    background: var(--stage);
    font-family: "Open Sans", Arial, sans-serif;
    display: flex;
    flex-direction: column;
    align-items: center;
    justify-content: center;
    gap: 56px;
  }
  .card {
    width: 560px;
    height: 320px;
    border-radius: 4px;
    box-shadow: 0 12px 30px rgba(0,0,0,0.35);
    position: relative;
    display: flex;
    flex-direction: column;
    align-items: center;
    justify-content: center;
  }
  .card--front { background: var(--card-dark); }
  .card--back { background: var(--card-light); }

  .brand { display: flex; align-items: center; gap: 14px; }
  .brand__disc {
    width: 46px; height: 46px; border-radius: 50%;
    background: var(--brand-sky);
  }
  .brand__name {
    font-weight: 700;
    font-size: 30px;
    letter-spacing: 0.5px;
    color: var(--brand-blue);
    text-transform: uppercase;
  }
  .card--back .brand { margin-bottom: 22px; }
  .card--back .brand__disc { width: 36px; height: 36px; }
  .card--back .brand__name { font-size: 20px; }

  .contact { text-align: center; line-height: 1.45; position: relative; width: 100%; }
  .contact__person { font-size: 15px; font-weight: 700; color: var(--brand-blue); text-transform: uppercase; }
  .contact__role { color: var(--brand-green); font-weight: 600; }
  .contact__line { font-size: 13.5px; color: var(--ink-grey); }
  .contact__label { color: var(--brand-blue); font-weight: 700; }

  .rule {
    position: absolute; height: 1px;
    background: linear-gradient(90deg, transparent, var(--rule-blue));
  }
  .rule--top { top: -8px; left: 340px; width: 170px;
    background: linear-gradient(90deg, var(--rule-blue), transparent); }
  .rule--bottom { bottom: -26px; left: 60px; width: 200px; }

  .social { display: flex; gap: 6px; justify-content: center; margin-top: 12px; }
  .social__dot { width: 22px; height: 22px; border-radius: 50%; background: var(--brand-blue); }
</style>
</head>
<body>
  <section class="card card--front" aria-label="Card front">
    <div class="brand">
      <span class="brand__disc"></span>
      <span class="brand__name">Tadd's Field Crafts</span>
    </div>
  </section>

  <section class="card card--back" aria-label="Card back">
    <div class="brand">
      <span class="brand__disc"></span>
      <span class="brand__name">Tadd's Field Crafts</span>
    </div>
    <div class="contact">
      <span class="rule rule--top"></span>
      <p class="contact__person">Dorian Hesk <span class="contact__role">- Director</span></p>
      <p class="contact__line"><span class="contact__label">Phone :</span> 0487253916 <span class="contact__label">Email :</span> dorian@tfcraft.biz</p>
      <p class="contact__line">www.taddsfieldcrafts.com</p>
      <div class="social" aria-label="Social profiles">
        <span class="social__dot"></span>
        <span class="social__dot"></span>
        <span class="social__dot"></span>
      </div>
      <span class="rule rule--bottom"></span>
    </div>
  </section>
</body>
</html>
```